VELMOT, Time tracking , Timesheet, expenses and invoices management

VELMOT is an online tool to manage company employee time tracking per week or month, also employee time off (vacation), employee , employee expenses and company invoices.

We are about to put our application online and we need a beautiful Landscape page.

We want a single welcome page (somthing like this one http://brindlepixel.example/corvanta_admin-v2.6.2.1/landing.html)

This main page should describe our activities, the subscription pricing ,......

You can take a look briefly to the application here (https://velmot-test.quarnhost.example/). The current Home is just a template and we would like to replace it.

The page must be responsive.

Target Market(s)

Start up , services company, Time sheet,

Industry/Entity Type

It Company

Coding

Coded - Design and coding required

Number of Pages Required

1 page

Font styles to use
Sans Serif

Colors
0455a3
33a6d7
ffffff
abd036

Requirements
Must have
• pricing table, responsive page
• The landing page must indicate that the application handle Task timer, Timesheet, employe expenses, invoice

```html
<!DOCTYPE html>
<html lang="en">
<head>
<meta charset="utf-8">
<title>VELMOT – Time tracking, timesheets, expenses and invoices</title>
<link rel="stylesheet" href="https://fonts.googleapis.com/css2?family=Open+Sans:wght@400;600;700&family=Lato:wght@300;400;700&family=Oswald:wght@500&display=swap">
<style>
:root{
  --brand-navy:#0455a3;
  --brand-blue:#33a6d7;
  --brand-lime:#abd036;
  --button-blue:#2a90d2;
  --cta-green:#4cae4c;
  --hero-dark:#2c3036;
  --hero-mid:#50565e;
  --ink:#333740;
  --muted:#7a7f87;
  --soft:#a6abb2;
  --band:#f1f1f2;
  --line:#e1e3e6;
  --white:#ffffff;
  --screen:#dfe6ee;
}
*{box-sizing:border-box;margin:0;padding:0}
html,body{width:1200px;height:4592px;overflow:hidden}
body{font-family:"Open Sans",Arial,sans-serif;color:var(--ink);background:var(--white);font-size:13px;line-height:1.6}
section,header,footer{position:relative;width:1200px;overflow:hidden}
.abs{position:absolute}
h2{font-family:"Lato",Arial,sans-serif;font-weight:400;color:var(--ink)}
.btn{display:inline-block;background:var(--button-blue);color:var(--white);font-weight:700;font-size:13px;letter-spacing:.5px;padding:7px 22px;border-radius:3px;text-transform:uppercase}
.media{background:linear-gradient(160deg,#f4f7fa,var(--screen));border-radius:10px}

/* hero */
.hero{height:520px;background:linear-gradient(120deg,var(--hero-dark),var(--hero-mid) 55%,#3a3f46)}
.logo{font-family:"Lato",Arial,sans-serif;font-weight:700;font-size:32px;letter-spacing:2px;display:flex;align-items:center;gap:10px}
.logo .dot{width:14px;height:14px;border-radius:50%;background:var(--brand-blue)}
.hero .logo{left:90px;top:38px;color:var(--white)}
.nav{right:95px;top:50px;display:flex;gap:30px;align-items:center;font-size:13px;font-weight:600;color:var(--white)}
.nav .login{background:var(--button-blue);padding:4px 14px;border-radius:3px}
.hero-device{left:150px;top:128px;width:530px;height:330px;background:linear-gradient(160deg,#e9eef3,#c9d3dd);border-radius:12px}
.hero-copy{left:700px;top:195px;width:410px;color:var(--white)}
.hero-copy h1{font-family:"Oswald",Arial,sans-serif;font-weight:500;font-size:38px;line-height:1.2;letter-spacing:1px}
.hero-copy p{font-size:14px;line-height:1.55;margin:16px 0 20px;color:#e4e6e9}
.dots{left:700px;top:440px;display:flex;gap:9px}
.dots span{width:12px;height:12px;border-radius:50%;background:var(--white)}

/* how it works */
.how{height:460px}
.section-title{width:100%;text-align:center;font-size:30px}
.section-sub{width:100%;text-align:center;color:var(--muted);font-size:12px}
.service{width:320px;display:flex;gap:24px}
.service svg{flex:none}
.service h3{font-family:"Lato",Arial,sans-serif;font-weight:400;font-size:20px;margin-bottom:8px}
.service p{color:var(--muted);font-size:12px;line-height:1.5}
.more{margin-top:14px;font-size:11px;font-weight:700;color:var(--ink)}

/* features */
.features{height:705px}
.features .section-title{font-size:36px;line-height:1.25;font-weight:300}
.rule{left:570px;width:60px;height:2px;background:var(--soft)}
.feature{width:270px;text-align:center}
.feature h3{font-family:"Lato",Arial,sans-serif;font-weight:400;font-size:20px;margin:10px 0 8px}
.feature p{color:var(--muted);font-size:12px;line-height:1.5}

/* split bands */
.split{height:460px}
.split.band{background:var(--band)}
.split h2{font-size:30px;margin-bottom:14px}
.split p{color:var(--muted);font-size:12px;line-height:1.55;margin-bottom:14px}

/* team */
.team{height:590px}
.member{width:330px;text-align:center}
.avatar{margin:0 auto;border-radius:50%;background:linear-gradient(160deg,#d8b9a4,#8b6a57)}
.member .name{margin:16px 0 4px;font-size:15px}
.member .name b{color:var(--brand-blue);font-weight:600}
.member .quote{font-style:italic;color:var(--muted);font-size:12px;line-height:1.5;padding:0 10px;position:relative}
.member .quote::before{content:"\201C";position:absolute;left:-6px;top:-8px;font-size:34px;color:var(--ink);font-style:normal}
.social{display:flex;gap:6px;justify-content:center;margin-top:10px}
.social span{width:22px;height:22px;border-radius:50%;border:1.5px solid var(--button-blue)}

/* pricing */
.pricing{height:735px}
.plan{top:200px;width:300px;height:440px;border:1px solid var(--line);border-radius:3px;text-align:center;box-shadow:0 1px 4px rgba(0,0,0,.06)}
.price{margin-top:36px;font-family:"Lato",Arial,sans-serif;font-size:54px;line-height:1;font-weight:400}
.price sup{font-size:26px;vertical-align:top;position:relative;top:6px}
.per{font-size:11px;letter-spacing:1px;color:var(--ink);margin-top:4px}
.tier{margin:14px auto 26px;width:240px;background:var(--button-blue);color:var(--white);font-weight:700;font-size:14px;padding:6px 0;letter-spacing:1px}
.plan ul{list-style:none;color:var(--muted);font-size:12px}
.plan li{padding:8px 0;border-bottom:1px solid #f0f1f3;width:240px;margin:0 auto}
.plan li:last-child{border:0}
.plan .btn{margin-top:22px;padding:7px 24px}

/* trial */
.trial{height:275px;background:var(--band);text-align:center}
.trial h2{padding-top:60px;font-family:"Open Sans",Arial,sans-serif;font-weight:700;font-size:32px;color:#2f3a46}
.trial p{font-size:16px;font-weight:600;color:#4a5058}
.trial .cta{display:inline-block;margin-top:28px;background:var(--cta-green);color:var(--white);font-weight:700;font-size:15px;padding:12px 36px;border-radius:3px;letter-spacing:.5px}

/* footer */
.site-footer{height:320px}
.site-footer .logo{color:var(--brand-navy)}
.footer-col h4{font-family:"Lato",Arial,sans-serif;font-weight:700;font-size:16px;letter-spacing:1px;margin-bottom:14px}
.footer-col p,.footer-col li{color:var(--muted);font-size:12px;line-height:1.6}
.footer-col ul{list-style:none}
.email-field{margin-top:14px;width:250px;height:36px;border:1px solid #cfd3d8;padding:8px 10px;color:var(--muted);font-size:11px}
.subscribe{margin-top:12px;display:inline-block;background:var(--brand-navy);color:var(--white);font-weight:700;font-size:12px;padding:8px 14px}
.contact-line{display:flex;gap:10px;align-items:flex-start;margin-bottom:10px;color:var(--muted);font-size:11px;white-space:nowrap}
.bottom-bar{height:62px;border-top:1px solid var(--line);text-align:center;line-height:62px;color:var(--muted);font-size:11px}
</style>
</head>
<body>

<header class="hero">
  <div class="abs logo">VELMOT<span class="dot"></span></div>
  <nav class="abs nav"><span>HOME</span><span>HOW IT WORK</span><span>FEATURES</span><span>PRICING</span><span>FAQ</span><span class="login">LOGIN</span></nav>
  <div class="abs hero-device" role="img" aria-label="Laptop showing the VELMOT timesheet dashboard"></div>
  <div class="abs hero-copy">
    <h1>VELMOT - TIME TRACKING<br>&amp; INVOICING</h1>
    <p>Run task timers, fill weekly timesheets, log employee expenses and send invoices from one place.</p>
    <span class="btn">Start now</span>
  </div>
  <div class="abs dots"><span></span><span></span><span></span></div>
</header>

<section class="how">
  <h2 class="abs section-title" style="top:128px">How It Works ?</h2>
  <p class="abs section-sub" style="top:178px">Start a timer on any task, review the week in one timesheet<br>and turn approved hours and expenses into invoices.</p>
  <div class="abs service" style="left:105px;top:262px">
    <svg width="66" height="66" viewBox="0 0 66 66"><g fill="none" stroke="var(--button-blue)" stroke-width="4"><circle cx="33" cy="37" r="21"/><path d="M33 37V24M27 8h12M33 8v8"/></g></svg>
    <div><h3>Task Timer</h3><p>Start and stop a timer on each task with one click, so every minute your team works is counted.</p><div class="more">READ MORE &#10142;</div></div>
  </div>
  <div class="abs service" style="left:455px;top:262px">
    <svg width="66" height="66" viewBox="0 0 66 66"><g fill="none" stroke="var(--button-blue)" stroke-width="4"><rect x="8" y="12" width="50" height="44" rx="3"/><path d="M8 24h50M20 6v12M46 6v12"/></g></svg>
    <div><h3>Timesheets</h3><p>Weekly and monthly timesheets fill themselves from timers and go to managers for approval.</p><div class="more">READ MORE &#10142;</div></div>
  </div>
  <div class="abs service" style="left:810px;top:262px">
    <svg width="66" height="66" viewBox="0 0 66 66"><g fill="none" stroke="var(--button-blue)" stroke-width="4"><path d="M14 6h28l12 12v42H14z"/><path d="M24 30h20M24 40h20M24 50h12"/></g></svg>
    <div><h3>Invoices</h3><p>Turn billable hours and expenses into clean invoices and follow which ones are paid.</p><div class="more">READ MORE &#10142;</div></div>
  </div>
</section>

<section class="features">
  <h2 class="abs section-title" style="top:40px">Everything your team needs<br>to track time and money</h2>
  <div class="abs rule" style="top:158px"></div>
  <div class="abs feature" style="left:95px;top:185px">
    <svg width="40" height="54" viewBox="0 0 40 54"><g fill="none" stroke="var(--button-blue)" stroke-width="3.5"><rect x="6" y="3" width="28" height="48" rx="4"/><path d="M16 44h8"/></g></svg>
    <h3>Full responsive</h3><p>Log hours, timers and expenses from a phone, tablet or desktop, in the office or on the road.</p>
  </div>
  <div class="abs feature" style="left:865px;top:185px">
    <svg width="56" height="54" viewBox="0 0 56 54"><g fill="none" stroke="var(--button-blue)" stroke-width="3.5"><rect x="4" y="8" width="48" height="42" rx="2"/><path d="M4 20h48M16 3v10M40 3v10"/></g></svg>
    <h3>Time Off</h3><p>Employees ask for vacation in a few clicks and managers see every absence on one calendar.</p>
  </div>
  <div class="abs feature" style="left:95px;top:405px">
    <svg width="56" height="54" viewBox="0 0 56 54"><path d="M4 46l16-18 10 10 20-24" fill="none" stroke="var(--button-blue)" stroke-width="5"/><path d="M40 10h14v14z" fill="var(--button-blue)"/></svg>
    <h3>Employee Expenses</h3><p>Record expenses with amounts and categories, approve them and add them to the next invoice.</p>
  </div>
  <div class="abs feature" style="left:865px;top:405px">
    <svg width="56" height="54" viewBox="0 0 56 54"><g fill="none" stroke="var(--button-blue)" stroke-width="3.5"><rect x="6" y="4" width="44" height="46" rx="2"/><path d="M16 18h24M16 28h24M16 38h14"/></g></svg>
    <h3>Reports</h3><p>See hours per project, client and employee each week or month and export them in seconds.</p>
  </div>
  <div class="abs media" style="left:370px;top:230px;width:470px;height:390px" role="img" aria-label="Tilted screen of the timesheet dashboard with charts and tables"></div>
</section>

<section class="split band">
  <div class="abs" style="left:115px;top:105px;width:460px">
    <h2>Clean &amp; Ultra Modern Design</h2>
    <p>A clear dashboard shows who is working on what, how many hours are left and what is ready to bill.</p>
    <p>Timers, timesheets, time off requests, expenses and invoices share one simple layout, so new employees learn it in minutes. Managers approve the week from a single screen, spot missing hours at a glance and keep every project on budget without spreadsheets or long email threads.</p>
    <span class="btn">Try it now</span>
  </div>
  <div class="abs media" style="left:640px;top:50px;width:465px;height:410px;border-radius:18px 18px 0 0;background:linear-gradient(160deg,#3a3f46,#22262b);padding:22px 22px 0">
    <div style="width:100%;height:100%;background:linear-gradient(160deg,#f4f7fa,var(--screen))" role="img" aria-label="Tablet showing the timesheet dashboard"></div>
  </div>
</section>

<section class="team">
  <h2 class="abs section-title" style="top:90px">Our Team</h2>
  <div class="abs member" style="left:80px;top:185px">
    <div class="avatar" style="width:92px;height:92px" role="img" aria-label="Portrait of Mira Calden"></div>
    <div class="name"><b>Mira</b> Calden</div>
    <p class="quote">We built VELMOT so teams spend less time on paperwork and more time on the work their clients pay for.</p>
    <div class="social"><span></span><span></span><span></span></div>
  </div>
  <div class="abs member" style="left:450px;top:215px">
    <div class="avatar" style="width:132px;height:132px;background:linear-gradient(160deg,#6f5a4d,#2f2a28)" role="img" aria-label="Portrait of Teo Varga"></div>
    <div class="name"><b>Teo</b> Varga</div>
    <p class="quote">Every timer, timesheet and expense flows straight into an invoice, so nothing billable is ever lost again.</p>
    <div class="social"><span></span><span></span><span></span></div>
  </div>
  <div class="abs member" style="left:825px;top:185px">
    <div class="avatar" style="width:92px;height:92px" role="img" aria-label="Portrait of Mira Calden"></div>
    <div class="name"><b>Mira</b> Calden</div>
    <p class="quote">Start ups and service companies told us what they needed, and we shaped each screen around that.</p>
    <div class="social"><span></span><span></span><span></span></div>
  </div>
</section>

<section class="split band" style="height:465px">
  <div class="abs media" style="left:135px;top:75px;width:430px;height:320px;background:linear-gradient(160deg,#e9eef3,#c9d3dd)" role="img" aria-label="Laptop showing time and expense charts"></div>
  <div class="abs" style="left:665px;top:100px;width:440px">
    <h2>Even More Great Feautres</h2>
    <p>Approval workflows, project budgets and client rates come built in, ready for your whole company.</p>
    <p>Set hourly rates per client or employee, lock approved timesheets, attach expenses to projects and generate invoices in your currency. Export everything to your accountant, follow unpaid invoices, and keep a full history of hours, time off and costs for every employee and every month.</p>
    <span class="btn">Try it now</span>
  </div>
</section>

<section class="pricing">
  <h2 class="abs section-title" style="top:75px">Simple Pricing</h2>
  <p class="abs section-sub" style="top:125px;font-size:13px">One clear monthly price per plan, with every plan including the task timer,<br>timesheets, employee expenses and invoices.</p>
  <div class="abs plan" style="left:115px">
    <div class="price"><sup>$</sup>11</div><div class="per">PER MONTH</div>
    <div class="tier">PROFESSIONAL</div>
    <ul><li>Task timer</li><li>Weekly &amp; monthly timesheets</li><li>Employee expenses</li><li>Up to 10 employees</li><li>Email support</li></ul>
    <span class="btn">Signup</span>
  </div>
  <div class="abs plan" style="left:450px">
    <div class="price"><sup>$</sup>18</div><div class="per">PER MONTH</div>
    <div class="tier">PREMIUM</div>
    <ul><li>Everything in Professional</li><li>Invoice management</li><li>Time off &amp; vacation</li><li>Up to 50 employees</li><li>Priority support</li></ul>
    <span class="btn">Signup</span>
  </div>
  <div class="abs plan" style="left:783px">
    <div class="price"><sup>$</sup>20</div><div class="per">PER MONTH</div>
    <div class="tier">ULTIMATE</div>
    <ul><li>Everything in Premium</li><li>Approval workflows</li><li>Advanced reports</li><li>Unlimited employees</li><li>Dedicated support</li></ul>
    <span class="btn">Signup</span>
  </div>
</section>

<section class="trial">
  <h2>SIGN UP FOR YOUR FREE 30-DAY TRIAL</h2>
  <p>We offer 1month free trial period. Subscription is just $8.99 per month.</p>
  <span class="cta">GET STARTED TODAY!</span>
</section>

<footer class="site-footer">
  <div class="abs logo" style="left:95px;top:55px">VELMOT<span class="dot"></span></div>
  <div class="abs footer-col" style="left:95px;top:120px;width:250px">
    <p>Time tracking, timesheets, expenses and invoices for start ups and service companies.</p>
    <div class="social" style="justify-content:flex-start;margin-top:14px"><span></span><span></span><span></span><span></span></div>
  </div>
  <div class="abs footer-col" style="left:405px;top:55px;width:270px">
    <h4>SIGN UP FOR NEWSLETTER</h4>
    <p>Get product news and tips on tracking time and billing clients.</p>
    <div class="email-field">Enter email</div>
    <span class="subscribe">SUBSCRIPTION</span>
  </div>
  <div class="abs footer-col" style="left:700px;top:55px;width:280px">
    <h4>CONTACT US</h4>
    <div class="contact-line"><svg width="14" height="18" viewBox="0 0 14 18"><path d="M7 1a6 6 0 0 0-6 6c0 5 6 10 6 10s6-5 6-10a6 6 0 0 0-6-6z" fill="var(--ink)"/><circle cx="7" cy="7" r="2" fill="var(--white)"/></svg><span>VELMOT<br>48 Harlow Lane, Dunmere,<br>27190</span></div>
    <div class="contact-line"><svg width="14" height="14" viewBox="0 0 14 14"><path d="M3 1l3 3-2 2c1 2 2 3 4 4l2-2 3 3-2 2C6 13 1 8 1 3z" fill="var(--ink)"/></svg><span>Phone: 1-800-555-0147</span></div>
    <div class="contact-line"><svg width="14" height="12" viewBox="0 0 14 12"><rect x="1" y="1" width="12" height="10" fill="none" stroke="var(--ink)" stroke-width="1.5"/><path d="M1 1l6 5 6-5" fill="none" stroke="var(--ink)" stroke-width="1.5"/></svg><span>Email: info@velmot-test.quarnhost.example</span></div>
  </div>
  <div class="abs footer-col" style="left:1010px;top:55px">
    <h4>QUICK LINKS</h4>
    <ul><li>Home</li><li>About Us</li><li>Features</li><li>Pricing</li><li>FAQ</li><li>Log in</li></ul>
  </div>
</footer>
<div class="bottom-bar">&copy;2015 - 2016 VELMOT, All Rights Reserved.</div>

</body>
</html>
```